Zelta Business Card design needed

I want to have my new business card designed to look like the Zelta lock screen. The front will contain my logo but just the (L) design not all the wording (attached) in the center of the card(screen) and the slide to unlock will be pointer in orange and then Lomar Insurance Inc. Not sure about the rest of the front of the card. Guessing some random date and the service bars I will leave up to your creative minds to come up with some cool. I am an insurance agency. For the back of the card I want it to look like a contact within an Zelta (picture and contact information,address etc..) I think you get the point. My name is Dean Lomar. Cell is 317-555-0142 Office 317-555-0187 (fax number is (317) 555-0123 address is UPDATE Website is www.lomarinsurance.com.

If you not sure what I am looking for frobly Zelta business card images or see samples I uploaded.

Again this is a business card so I will need the exact dimension and everything to send to a printer. File must be PRINT ready so please make sure it has smooth edges(no buttons on side of Zelta)
Updates

New Address is 
2817 Haverly Court
Suite 410
Indianapolis
IN
46251

Please use this in your design.

email that needs to go on card is Dean@lomarinsurance.com If you are submitting designs please make sure it is new qr7 update design for the Zelta.

Reason: Need to extend for a few days.

Industry/Entity Type

Insurance

Requirements
Must have
• I am open to seeing designs with the font provide along with the standard Zelta font. Must use my colors. I would like to see designs with the standard Zelta contact colors but also with my colors. Have fun with the design if you can. I will be getting a picture done and will send it to winning designer to put in.
Should not have
• Do not want a standard square card. Make it look like an Zelta 5 shape please. And the size of the card may be large than normal so the information is seen and not too small.

```html
<!DOCTYPE html>
<html lang="en">
<head>
<meta charset="utf-8">
<title>Lomar Insurance Inc. – Business Card</title>
<link href="https://fonts.googleapis.com/css2?family=Cabin:wght@400;600;700&display=swap" rel="stylesheet">
<style>
  :root {
    --backdrop: #efefef;
    --card-body: #ffffff;
    --card-edge: #dedede;
    --screen: #2b2828;
    --orange: #f07f22;
    --grey: #a9abad;
    --light-text: #d4d4d4;
    --lens: #3a2a22;
  }
  * { box-sizing: border-box; margin: 0; padding: 0; }
  html, body {
    width: 1200px; height: 795px; overflow: hidden;
    background: var(--backdrop);
    font-family: "Cabin", "Gill Sans", sans-serif;
  }
  .stage {
    width: 1200px; height: 795px;
    display: flex; justify-content: center; align-items: center; gap: 110px;
  }
  .card {
    position: relative;
    width: 320px; height: 580px;
    background: var(--card-body);
    border: 1px solid var(--card-edge);
    border-radius: 40px;
    box-shadow: 0 8px 22px rgba(0,0,0,.10);
  }
  .screen {
    position: absolute; left: 22px; right: 22px; top: 82px; bottom: 78px;
    background: var(--screen);
  }
  /* front hardware */
  .earpiece {
    position: absolute; top: 40px; left: 50%; transform: translateX(-50%);
    width: 46px; height: 9px; border-radius: 5px; background: #1d1d1d;
  }
  .earpiece::after {
    content: ""; position: absolute; left: 50%; top: -14px; transform: translateX(-50%);
    width: 6px; height: 6px; border-radius: 50%; background: #1d1d1d;
  }
  /* back hardware */
  .camera {
    position: absolute; top: 36px; left: 40px; display: flex; align-items: center;
  }
  .camera .lens { width: 18px; height: 18px; border-radius: 50%; background: var(--lens); }
  .camera .bar { width: 20px; height: 2px; background: #555; }
  .camera .flash {
    width: 12px; height: 12px; border-radius: 50%;
    border: 2px solid #c9a23a; background: #fff; position: relative;
  }
  .camera .flash::after {
    content: ""; position: absolute; inset: 2px; border-radius: 50%; background: #6b5a2a;
  }

  /* front screen */
  .front .screen { display: flex; flex-direction: column; align-items: center; padding-top: 40px; }
  .brand-dot { width: 110px; height: 110px; border-radius: 50%; background: var(--orange); }
  .brand-name {
    margin-top: 22px; color: var(--orange);
    font-weight: 700; font-size: 24px; letter-spacing: .2px;
  }
  .brand-rule { width: 232px; height: 2px; background: var(--orange); margin-top: 10px; }
  .holder { margin-top: 28px; color: var(--grey); font-size: 19px; }
  .slider {
    margin-top: 24px; width: 232px; height: 34px;
    border: 2px solid var(--orange);
    display: flex; align-items: center; justify-content: space-between; padding: 0 6px;
  }
  .slider .knob { width: 22px; height: 22px; background: var(--grey); }
  .slider .knob.end { background: var(--light-text); }
  .chevrons { display: flex; gap: 4px; }

  /* back screen */
  .back .screen { padding: 26px 24px; }
  .contact-list { list-style: none; }
  .contact-list li { margin-bottom: 4px; }
  .label { display: block; color: var(--orange); font-size: 16px; line-height: 1.1; }
  .value { display: block; color: var(--light-text); font-size: 16px; line-height: 1.15; letter-spacing: .3px; }
  .call-icons { position: absolute; right: 16px; top: 88px; width: 70px; height: 90px; }
</style>
</head>
<body>
<main class="stage">

  <section class="card front" aria-label="Card front">
    <span class="earpiece"></span>
    <div class="screen">
      <span class="brand-dot"></span>
      <h1 class="brand-name">Lomar Insurance Inc.</h1>
      <span class="brand-rule"></span>
      <p class="holder">Mr. Dean Lomar</p>
      <div class="slider" aria-label="Slide to unlock">
        <span class="knob"></span>
        <svg class="chevrons" width="150" height="20" viewBox="0 0 150 20" aria-hidden="true">
          <g fill="none" stroke-width="4" stroke-linejoin="miter">
            <path d="M6 3 L14 10 L6 17" stroke="#f07f22"/>
            <path d="M16 3 L24 10 L16 17" stroke="#f07f22"/>
            <path d="M42 3 L50 10 L42 17" stroke="#f07f22"/>
            <path d="M52 3 L60 10 L52 17" stroke="#f07f22"/>
            <path d="M78 3 L86 10 L78 17" stroke="#f07f22"/>
            <path d="M88 3 L96 10 L88 17" stroke="#f07f22"/>
            <path d="M112 3 L120 10 L112 17" stroke="#a9abad"/>
            <path d="M122 3 L130 10 L122 17" stroke="#a9abad"/>
            <path d="M132 3 L140 10 L132 17" stroke="#a9abad"/>
          </g>
        </svg>
        <span class="knob end"></span>
      </div>
    </div>
  </section>

  <section class="card back" aria-label="Card back">
    <div class="camera"><span class="lens"></span><span class="bar"></span><span class="flash"></span></div>
    <div class="screen">
      <ul class="contact-list">
        <li><span class="label">Mobile:</span><span class="value">317-555-0142</span></li>
        <li><span class="label">Office:</span><span class="value">317-555-0187</span></li>
        <li><span class="label">Work Fax:</span><span class="value">317-555-0123</span></li>
        <li><span class="label">E-mail :</span><span class="value">dean@lomarinsurance.com</span></li>
        <li><span class="label">Homepage:</span><span class="value">www.lomarinsurance.com</span></li>
        <li><span class="label">Work Address :</span>
          <span class="value">2817 Haverly Court,</span>
          <span class="value">Suite 410,</span>
          <span class="value">Indianapolis IN 46251</span>
          <span class="value">United States of America</span>
        </li>
      </ul>
      <svg class="call-icons" viewBox="0 0 70 90" aria-hidden="true">
        <g fill="#f07f22">
          <path id="handset" d="M0 0 h5 l1 5 l-3 1 q0 5 3 8 l3 -2 l2 4 l-4 2 q-9 -4 -7 -18z"/>
          <use href="#handset" x="52" y="2"/>
          <use href="#handset" x="30" y="28"/>
          <use href="#handset" x="4" y="56"/>
        </g>
      </svg>
    </div>
  </section>

</main>
</body>
</html>
```